Natural Skincare Product Labels Design

We are looking for a designer to create elegant but quirky, functional product labels for our natural skincare range.
The labels must reflect our brand’s values of simplicity, luxury, and the natural, handmade essence of our products.
https://www.instagram.com/tolvarenskincare
1. Key Details
Packaging Dimensions
Container Types: Transparent jars.
Sizes for Body Products:
Diameter: 64mm–68mm.
Heights: 80mm, 88mm, and 97mm (lid height: 15mm).
Sizes for Face Creams:
Diameter: 60mm.
Height: 50mm (lid height: 15mm).
Label Fit: For body products, ideally one label size to fit all jar sizes.
For the smaller face cream jars, a separate, tailored label is required.
2. Label Placement
Options include a wrapped-around label or a combination of wrapped-around and top-of-jar elements.
Transparent jars mean the label must leave space for the product to be visible (e.g., partial wrap or cutout areas).
3. Content Requirements
Product Name: Prominently displayed.
Ingredient List: Dedicated space required.
Disclaimer/Usage Instructions: Include space for this information.
4. Design Goals
Look & Feel: Simple, upmarket, and natural, with a handmade essence.
Logo Usage: Our logo is finalized and available in gold, black, and white variants. Use Josefin Bold font for the logo if adjustments are required.
Color Palette: Neutral tones (e.g., whites, blacks, golds) are preferred, with flexibility for subtle pops of color tied to each product’s main ingredient.
5. Imagery
Open to including images and colours (e.g., botanical illustrations) that highlight the main ingredient (e.g., coffee beans, turmeric root, or honeycomb). Also open to labels having a prominent colour to tie it in to the main ingredient.
Alternatively, no images can also work for a clean design.
6. Current Design Context
Our temporary design features gold leaf on top and a simple handmade side label. We’re seeking to elevate this to a more polished, cohesive design.
7. Product Line
- Body Products (Larger Jars)
Mivo Body Butter
Key Ingredients: Guarana & Cupuaçu butter (inspired by Brazil).
Note: “Mivo” is slang for “bum.”
Manuka Honey Body Butter
Key Ingredients: Manuka honey (from New Zealand) & Cupuaçu butter.
Coffee Body Scrub
Key Ingredients: Coffee and Demerara sugar.
Whipped Body Soap - Turmeric
Key Ingredients: Turmeric and Bentonite clay.
Whipped Body Soap - Banana
- Face Products (Smaller Jars)
Face Cream
Key Ingredients: Carrot Oil and Raspberry Oil.
Features natural UV protection.
Good Night Cream
Key Ingredients: Enriched with Magnesium.
Promotes relaxation and restful sleep.
8. Submission Guidelines
Flexibility: Design should allow for consistent branding across all products while accommodating the varying jar sizes and ingredient focus.
Material Considerations: Labels should complement the transparent jars and allow the product inside to remain partially visible.
Print Elements: Incorporating gold accents is a plus but should not overpower the design.
We’re excited to see your vision for a label that celebrates the natural beauty and high quality of our skincare range. Please include mockups to showcase the design in use, particularly on transparent jars of varying sizes.
women 20-50 years of age

```html
<!DOCTYPE html>
<html lang="en">
<head>
<meta charset="utf-8">
<title>Tolvaren Natural Skincare – Face Labels</title>
<link rel="stylesheet" href="https://fonts.googleapis.com/css2?family=Josefin+Sans:wght@400;600;700&family=Roboto+Condensed:wght@400;700&display=swap">
<style>
  :root {
    --stage: #ababab;
    --black: #050505;
    --gold: #c9a43a;
    --paper: #ffffff;
    --ink: #1a1a1a;
    --night-light: #f3eee7;
    --night-dark: #c6b6a3;
    --rose-light: #ea1250;
    --rose-dark: #64040f;
    --rose-ink: #2a0208;
    --panel-light: #f4f4f4;
    --panel-dark: #9b9b9b;
  }
  * { box-sizing: border-box; margin: 0; padding: 0; }
  html, body { width: 1200px; height: 1200px; overflow: hidden; }
  body {
    background: var(--stage);
    display: flex;
    flex-direction: column;
    justify-content: center;
    align-items: center;
    gap: 90px;
  }
  .label {
    width: 1080px;
    height: 400px;
    display: grid;
    grid-template-columns: 250px 580px 250px;
    box-shadow: 0 6px 24px rgba(0,0,0,0.18);
  }
  .info-panel {
    background: var(--paper);
    padding: 22px 18px;
    font-family: "Roboto Condensed", Arial Narrow, sans-serif;
    font-size: 12.5px;
    line-height: 1.55;
    color: var(--ink);
    display: flex;
    flex-direction: column;
    justify-content: space-between;
  }
  .disclaimer-box {
    border: 1px solid var(--ink);
    padding: 10px 10px;
  }
  .front-panel {
    display: grid;
    grid-template-rows: 150px 1fr 44px;
    background: var(--black);
  }
  .brand-block {
    display: flex;
    flex-direction: column;
    align-items: center;
    justify-content: flex-end;
    padding-bottom: 20px;
  }
  .brand-name {
    font-family: "Josefin Sans", sans-serif;
    font-weight: 400;
    font-size: 24px;
    letter-spacing: 0.22em;
    color: var(--gold);
  }
  .title-band {
    border-top: 2px solid var(--gold);
    border-bottom: 2px solid var(--gold);
    display: flex;
    flex-direction: column;
    align-items: center;
    justify-content: center;
    text-align: center;
    font-family: "Josefin Sans", sans-serif;
    color: var(--black);
  }
  .night .title-band { background: linear-gradient(90deg, var(--night-light), var(--night-dark)); }
  .rose .title-band { background: linear-gradient(90deg, var(--rose-light), var(--rose-dark)); }
  .range-name { font-size: 19px; letter-spacing: 0.06em; }
  .product-name {
    font-size: 50px;
    font-weight: 400;
    letter-spacing: 0.03em;
    margin: 8px 0 14px;
  }
  .claims { font-size: 19px; letter-spacing: 0.05em; line-height: 1.45; }
  .rose .range-name, .rose .claims { color: var(--rose-ink); }
  .claims .lower { text-transform: none; }
  .net-weight {
    font-family: "Roboto Condensed", Arial Narrow, sans-serif;
    color: var(--gold);
    font-size: 17px;
    display: flex;
    align-items: center;
    justify-content: center;
  }
  .directions-panel {
    background: linear-gradient(90deg, var(--panel-light), var(--panel-dark));
    padding: 22px 18px;
    font-family: "Roboto Condensed", Arial Narrow, sans-serif;
    font-size: 12.5px;
    line-height: 1.55;
    color: var(--ink);
    display: flex;
    flex-direction: column;
    justify-content: space-between;
  }
  .badge-row { display: flex; gap: 12px; justify-content: flex-end; }
</style>
</head>
<body>

<section class="label night">
  <div class="info-panel">
    <p>INGREDIENTS: Shea butter, jojoba oil, magnesium chloride, aloe leaf juice, sweet almond oil, cocoa butter, vitamin E, lavender oil, chamomile extract, beeswax, rosehip oil, glycerin, natural fragrance.</p>
    <p class="disclaimer-box">For external use only. Patch test before first use. Avoid contact with eyes. Stop use if irritation occurs. Store in a cool, dry place away from sunlight.</p>
  </div>
  <div class="front-panel">
    <div class="brand-block"><span class="brand-name">TOLVAREN</span></div>
    <div class="title-band">
      <p class="range-name">NATURAL SKINCARE</p>
      <h1 class="product-name">GOOD NIGHT CREAM</h1>
      <p class="claims">ENRICHED <span class="lower">with</span> MAGNESIUM<br>PROMOTES RELAXATION &amp; RESTFUL SLEEP</p>
    </div>
    <div class="net-weight">Net. Wt. 33g</div>
  </div>
  <div class="directions-panel">
    <p>DIRECTIONS: Apply a small amount to clean skin each evening before bed. Massage gently in upward circles until absorbed. Use nightly for best results.</p>
    <svg class="badge-row" width="214" height="60" viewBox="0 0 214 60" aria-hidden="true">
      <circle cx="30" cy="30" r="25" fill="none" stroke="#1a1a1a" stroke-width="2.5"/>
      <circle cx="107" cy="30" r="25" fill="none" stroke="#1a1a1a" stroke-width="2.5"/>
      <circle cx="184" cy="30" r="25" fill="#1a1a1a"/>
    </svg>
  </div>
</section>

<section class="label rose">
  <div class="info-panel">
    <p>INGREDIENTS: Shea butter, carrot seed oil, raspberry seed oil, aloe leaf juice, jojoba oil, cocoa butter, vitamin E, rosehip oil, beeswax, glycerin, calendula extract.</p>
    <p class="disclaimer-box">For external use only. Patch test before first use. Avoid contact with eyes. Stop use if irritation occurs. Store in a cool, dry place away from sunlight.</p>
  </div>
  <div class="front-panel">
    <div class="brand-block"><span class="brand-name">TOLVAREN</span></div>
    <div class="title-band">
      <p class="range-name">NATURAL SKINCARE</p>
      <h1 class="product-name">FACE CREAM</h1>
      <p class="claims"><span class="lower">with</span> CARROT OIL &amp; RASPBERRY OIL<br>FEATURES NATURAL UV PROTECTION</p>
    </div>
    <div class="net-weight">Net. Wt. 33g</div>
  </div>
  <div class="directions-panel">
    <p>DIRECTIONS: Apply a small amount to clean face and neck each morning. Massage gently in upward circles until absorbed. Use daily for best results.</p>
    <svg class="badge-row" width="214" height="60" viewBox="0 0 214 60" aria-hidden="true">
      <circle cx="30" cy="30" r="25" fill="none" stroke="#1a1a1a" stroke-width="2.5"/>
      <circle cx="107" cy="30" r="25" fill="none" stroke="#1a1a1a" stroke-width="2.5"/>
      <circle cx="184" cy="30" r="25" fill="#1a1a1a"/>
    </svg>
  </div>
</section>

</body>
</html>
```